Ombrel Luxury Charters - Business Card Design

Please design a business card with the following information and logo:

Tessa Okonkwo
412-638-2071
519-204-8836
ig logo @ombrel_charters
info@ velquorinmarine.com
www.OmbrelCharters.com

Please submit high resolution files
Editable AI, PDF, and JPG
3.5" wide x 2" high with .25" inches of bleed for printing

Thank you and good luck to all!

```html
<!DOCTYPE html>
<html lang="en">
<head>
<meta charset="utf-8">
<title>Ombrel Luxury Charters – Business Card</title>
<link rel="stylesheet" href="https://fonts.googleapis.com/css2?family=Montserrat:wght@500;600;800&family=Roboto:wght@400&display=swap">
<style>
  :root {
    --page: #e6e8eb;
    --navy: #132f5a;
    --navy-deep: #0e2549;
    --amber: #f2a01e;
    --rule: #8a6a3a;
  }
  * { margin: 0; padding: 0; box-sizing: border-box; }
  html, body { width: 1200px; height: 900px; overflow: hidden; }
  body {
    background: var(--page);
    display: flex;
    flex-direction: column;
    align-items: center;
    justify-content: center;
    gap: 40px;
    font-family: "Roboto", Arial, sans-serif;
  }
  .card {
    width: 700px;
    height: 400px;
    border-radius: 26px;
    background: linear-gradient(160deg, var(--navy) 0%, var(--navy-deep) 100%);
    position: relative;
    box-shadow: 0 10px 24px rgba(10, 25, 50, 0.25);
  }
  .brand-name {
    font-family: "Montserrat", Arial, sans-serif;
    font-weight: 600;
    color: var(--amber);
    text-transform: uppercase;
    text-align: center;
    line-height: 1.15;
  }

  /* Front */
  .card-front .brand-name {
    position: absolute;
    left: 40px;
    top: 150px;
    width: 200px;
    font-size: 28px;
    letter-spacing: 3px;
  }
  .card-front .brand-name small {
    display: block;
    font-size: 13px;
    letter-spacing: 2px;
    margin-top: 6px;
  }
  .holder {
    position: absolute;
    left: 290px;
    top: 48px;
    right: 40px;
  }
  .holder-name {
    font-family: "Montserrat", Arial, sans-serif;
    font-weight: 800;
    font-size: 34px;
    color: var(--amber);
    text-transform: uppercase;
    letter-spacing: 0.5px;
  }
  .holder-title {
    font-family: "Montserrat", Arial, sans-serif;
    font-weight: 500;
    font-size: 19px;
    color: var(--amber);
    margin-top: 6px;
  }
  .holder-rule {
    height: 1px;
    background: var(--rule);
    margin-top: 26px;
    width: 320px;
  }
  .contacts {
    position: absolute;
    left: 290px;
    top: 196px;
    list-style: none;
  }
  .contact {
    display: flex;
    align-items: flex-start;
    gap: 14px;
    color: var(--amber);
    font-size: 17px;
    line-height: 22px;
    margin-bottom: 8px;
  }
  .contact-icon {
    width: 22px;
    height: 22px;
    flex: none;
  }

  /* Back */
  .card-back {
    display: flex;
    align-items: center;
    justify-content: center;
  }
  .card-back .brand-name {
    font-size: 58px;
    letter-spacing: 6px;
  }
  .card-back .brand-name small {
    display: block;
    font-size: 22px;
    letter-spacing: 5px;
    margin-top: 10px;
  }
</style>
</head>
<body>

  <section class="card card-front" aria-label="Business card front">
    <div class="brand-name">Ombrel<small>Luxury Charters</small></div>

    <div class="holder">
      <h1 class="holder-name">Tessa Okonkwo</h1>
      <p class="holder-title">Managing Director</p>
      <div class="holder-rule"></div>
    </div>

    <ul class="contacts">
      <li class="contact">
        <svg class="contact-icon" viewBox="0 0 22 22" aria-hidden="true">
          <circle cx="11" cy="11" r="11" fill="var(--amber)"/>
          <path d="M7.2 5.5l2 2.2-1 1.3c.7 1.6 1.9 2.8 3.5 3.6l1.3-1 2.2 2-1.1 1.8c-3.9-.5-7.3-3.9-7.9-7.9z" fill="var(--navy)"/>
        </svg>
        <span>412-638-2071<br>519-204-8836</span>
      </li>
      <li class="contact">
        <svg class="contact-icon" viewBox="0 0 22 22" aria-hidden="true">
          <circle cx="11" cy="11" r="11" fill="var(--amber)"/>
        </svg>
        <span>@ombrel_charters</span>
      </li>
      <li class="contact">
        <svg class="contact-icon" viewBox="0 0 22 22" aria-hidden="true">
          <circle cx="11" cy="11" r="11" fill="var(--amber)"/>
          <rect x="5.5" y="7" width="11" height="8" rx="1" fill="var(--navy)"/>
          <path d="M5.8 7.4L11 11.5l5.2-4.1" stroke="var(--amber)" stroke-width="1" fill="none"/>
        </svg>
        <span>info@velquorinmarine.com</span>
      </li>
      <li class="contact">
        <svg class="contact-icon" viewBox="0 0 22 22" aria-hidden="true">
          <circle cx="11" cy="11" r="11" fill="var(--amber)"/>
          <g stroke="var(--navy)" stroke-width="1.2" fill="none">
            <circle cx="11" cy="11" r="5.5"/>
            <ellipse cx="11" cy="11" rx="2.4" ry="5.5"/>
            <path d="M5.5 11h11"/>
          </g>
        </svg>
        <span>www.OmbrelCharters.com</span>
      </li>
    </ul>
  </section>

  <section class="card card-back" aria-label="Business card back">
    <div class="brand-name">Ombrel<small>Luxury Charters</small></div>
  </section>

</body>
</html>
```